Insurance Agency Flyer

Create a flyer that encompasses the basic services that our agency offers. Flyer wording, logo, and company font are attached. See our website at www.tavenmork.com for additional details.

Target Market(s)

Prospective clients

Industry/Entity Type

Insurance Agency

Other font styles liked:
• baker signet com

```html
<!DOCTYPE html>
<html lang="en">
<head>
<meta charset="utf-8">
<title>The Tavenmork Company – Insurance Flyer</title>
<link href="https://fonts.googleapis.com/css2?family=Open+Sans:ital,wght@0,300;0,400;0,600;0,700;1,300;1,400&family=Crimson+Text&display=swap" rel="stylesheet">
<style>
  :root {
    --red: #e5001e;
    --ink: #333333;
    --muted: #555555;
    --paper: #ffffff;
    --panel-left: #dcdcdc;
    --panel-right: #ececec;
    --charcoal: #3b3b3b;
    --backdrop: #f1f1ef;
  }
  * { box-sizing: border-box; margin: 0; padding: 0; }
  html, body { width: 1200px; height: 885px; overflow: hidden; }
  body { background: var(--backdrop); font-family: "Open Sans", Arial, sans-serif; color: var(--ink); }

  .flyer {
    position: absolute; left: 300px; top: 20px;
    width: 600px; height: 845px; background: var(--paper);
    overflow: hidden;
  }

  .hero-photo {
    height: 154px;
    background: linear-gradient(100deg, #cfd3d6 0%, #eef0f1 35%, #e3e5e6 60%, #bcc1c5 100%);
  }

  .about { position: relative; height: 123px; background: var(--paper); }
  .brand {
    position: absolute; left: 24px; top: 50px;
    display: flex; align-items: center; gap: 6px;
  }
  .brand-dot { width: 22px; height: 22px; border-radius: 50%; background: var(--red); }
  .brand-name { font-weight: 700; font-size: 17px; color: var(--red); }
  .about-divider {
    position: absolute; left: 152px; top: 20px; width: 1px; height: 86px; background: #bdbdbd;
  }
  .about-copy { position: absolute; left: 196px; top: 14px; width: 352px; }
  .about-title { font-weight: 400; font-size: 20px; line-height: 1.3; color: var(--red); margin-bottom: 8px; }
  .about-text { font-family: "Crimson Text", Georgia, serif; font-size: 11px; line-height: 1.32; color: var(--muted); }

  .accent-bar { position: relative; height: 10px; background: var(--red); }
  .accent-notch { position: absolute; left: 284px; top: 10px; }
  .strip-photo { height: 12px; background: linear-gradient(90deg, #9aa0a5, #d5d8da 45%, #8e949a); }

  .services { display: flex; height: 359px; }
  .col { width: 300px; padding: 28px 28px 0 30px; }
  .col-left { background: var(--panel-left); }
  .col-right { background: var(--panel-right); padding-left: 17px; padding-right: 4px; }
  .col-title { font-weight: 400; font-size: 18px; line-height: 1.2; color: var(--red); padding-bottom: 12px; border-bottom: 1px solid #a9a9a9; width: 232px; white-space: nowrap; }
  .intro-text { font-family: "Crimson Text", Georgia, serif; font-size: 11.5px; line-height: 1.5; color: var(--ink); margin-top: 12px; }
  .sub-title { font-weight: 400; font-size: 11.5px; color: var(--red); margin: 16px 0 6px; white-space: nowrap; }
  .fine-text { font-size: 6.6px; line-height: 1.42; color: var(--ink); }

  .group-label { font-weight: 600; font-size: 8px; letter-spacing: 0.3px; color: var(--ink); margin: 16px 0 6px; }
  .group-label.business { margin-top: 22px; }
  .coverage-list { display: grid; grid-template-columns: 142px 1fr; row-gap: 5px; list-style: none; }
  .coverage-list li { display: flex; align-items: center; gap: 5px; font-weight: 600; font-size: 7.8px; letter-spacing: -0.1px; color: var(--ink); white-space: nowrap; height: 13px; }
  .tick { width: 11px; height: 11px; flex: none; }

  .testimonial-row { display: flex; height: 153px; }
  .meeting-photo { width: 300px; background: linear-gradient(135deg, #dfe6ea 0%, #8f9aa3 45%, #3e4a55 100%); }
  .testimonial { width: 300px; background: var(--charcoal); padding: 22px 20px 0 38px; }
  .quote { font-style: italic; font-weight: 300; font-size: 10.6px; line-height: 1.3; color: #f3f3f3; }
  .quote-name { font-weight: 700; font-size: 9px; color: #ffffff; margin-top: 14px; }
  .quote-role { font-style: italic; font-size: 8.5px; color: var(--red); }

  .footer {
    height: 36px; background: var(--red);
    display: flex; align-items: center; justify-content: space-between; padding: 0 16px 0 34px;
  }
  .footer-url { font-weight: 600; font-size: 10px; color: #ffffff; }
  .footer-brand { display: flex; align-items: center; gap: 5px; }
  .footer-dot { width: 14px; height: 14px; border-radius: 50%; background: #ffffff; }
  .footer-name { font-weight: 700; font-size: 11px; color: #ffffff; }
</style>
</head>
<body>
<main class="flyer">
  <div class="hero-photo" role="img" aria-label="Photo of three smiling insurance agents in an office"></div>

  <section class="about">
    <div class="brand">
      <span class="brand-dot"></span>
      <span class="brand-name">Tavenmork</span>
    </div>
    <div class="about-divider"></div>
    <div class="about-copy">
      <h1 class="about-title">About Our Agency</h1>
      <p class="about-text">Established in 2008, The Tavenmork Company was created on the premise that both business and individual consumers should expect more from their insurance agency and agents. The Tavenmork Company is a full-service insurance agency that specializes in tailored insurance protection, risk management, and claims consultation.</p>
    </div>
  </section>

  <div class="accent-bar">
    <svg class="accent-notch" width="32" height="10" viewBox="0 0 32 10"><polygon points="0,0 32,0 16,10" fill="var(--red)"/></svg>
  </div>
  <div class="strip-photo" role="img" aria-label="Photo strip of a business handshake"></div>

  <section class="services">
    <div class="col col-left">
      <h2 class="col-title">A Professional Agency With<br>Exceptional Service</h2>
      <p class="intro-text">The Tavenmork Company is a firm of proven professionals who are dedicated to caring and conscientious service. We are committed to a high standard of excellence in all that we do and strive to establish a firm relationship of mutual trust and service with each of our clients.</p>
      <h3 class="sub-title">We Are An Independent Assured Choice Agency</h3>
      <p class="fine-text">Being an Independent Assured Choice Agency means that we take our time to make sure that we learn about your needs, and that each policy is built to specifically meet those needs. We are committed to treating you as a person, not another policy number. We will work with you to identify the insurance products and services that are right for you, your family, and/or your business. We accomplish this by using our expertise and multiple insurance carrier relationships to customize your insurance program. We will explain the different coverage and options available to you, and should the need arise, we will be there to guide you through the claims process. Our promise to you is that we will return your phone calls and emails promptly and respond to your requests in a timely manner. Also, we work diligently to stay informed about the latest insurance trends to understand how they might affect our clients.</p>
    </div>

    <div class="col col-right">
      <h2 class="col-title">We Offer<br>Complete Insurance Services:</h2>

      <h3 class="group-label">PERSONAL COVERAGES</h3>
      <ul class="coverage-list">
        <li><svg class="tick" viewBox="0 0 12 12"><circle cx="6" cy="6" r="6" fill="var(--red)"/><path d="M3.2 6.2l1.9 1.9 3.7-3.8" fill="none" stroke="#fff" stroke-width="1.5"/></svg>Homeowners</li>
        <li><svg class="tick" viewBox="0 0 12 12"><circle cx="6" cy="6" r="6" fill="var(--red)"/><path d="M3.2 6.2l1.9 1.9 3.7-3.8" fill="none" stroke="#fff" stroke-width="1.5"/></svg>Valuable Property</li>
        <li><svg class="tick" viewBox="0 0 12 12"><circle cx="6" cy="6" r="6" fill="var(--red)"/><path d="M3.2 6.2l1.9 1.9 3.7-3.8" fill="none" stroke="#fff" stroke-width="1.5"/></svg>Automobile</li>
        <li><svg class="tick" viewBox="0 0 12 12"><circle cx="6" cy="6" r="6" fill="var(--red)"/><path d="M3.2 6.2l1.9 1.9 3.7-3.8" fill="none" stroke="#fff" stroke-width="1.5"/></svg>Life</li>
        <li><svg class="tick" viewBox="0 0 12 12"><circle cx="6" cy="6" r="6" fill="var(--red)"/><path d="M3.2 6.2l1.9 1.9 3.7-3.8" fill="none" stroke="#fff" stroke-width="1.5"/></svg>Renters / Condo</li>
        <li><svg class="tick" viewBox="0 0 12 12"><circle cx="6" cy="6" r="6" fill="var(--red)"/><path d="M3.2 6.2l1.9 1.9 3.7-3.8" fill="none" stroke="#fff" stroke-width="1.5"/></svg>Disability</li>
        <li><svg class="tick" viewBox="0 0 12 12"><circle cx="6" cy="6" r="6" fill="var(--red)"/><path d="M3.2 6.2l1.9 1.9 3.7-3.8" fill="none" stroke="#fff" stroke-width="1.5"/></svg>Personal umbrella</li>
        <li><svg class="tick" viewBox="0 0 12 12"><circle cx="6" cy="6" r="6" fill="var(--red)"/><path d="M3.2 6.2l1.9 1.9 3.7-3.8" fill="none" stroke="#fff" stroke-width="1.5"/></svg>Health</li>
      </ul>

      <h3 class="group-label business">BUSINESS COVERAGES</h3>
      <ul class="coverage-list">
        <li><svg class="tick" viewBox="0 0 12 12"><circle cx="6" cy="6" r="6" fill="var(--red)"/><path d="M3.2 6.2l1.9 1.9 3.7-3.8" fill="none" stroke="#fff" stroke-width="1.5"/></svg>Commercial General Liability</li>
        <li><svg class="tick" viewBox="0 0 12 12"><circle cx="6" cy="6" r="6" fill="var(--red)"/><path d="M3.2 6.2l1.9 1.9 3.7-3.8" fill="none" stroke="#fff" stroke-width="1.5"/></svg>Professional Liability</li>
        <li><svg class="tick" viewBox="0 0 12 12"><circle cx="6" cy="6" r="6" fill="var(--red)"/><path d="M3.2 6.2l1.9 1.9 3.7-3.8" fill="none" stroke="#fff" stroke-width="1.5"/></svg>Commercial Property</li>
        <li><svg class="tick" viewBox="0 0 12 12"><circle cx="6" cy="6" r="6" fill="var(--red)"/><path d="M3.2 6.2l1.9 1.9 3.7-3.8" fill="none" stroke="#fff" stroke-width="1.5"/></svg>Employment Practices Liability</li>
        <li><svg class="tick" viewBox="0 0 12 12"><circle cx="6" cy="6" r="6" fill="var(--red)"/><path d="M3.2 6.2l1.9 1.9 3.7-3.8" fill="none" stroke="#fff" stroke-width="1.5"/></svg>Workers' Compensation</li>
        <li><svg class="tick" viewBox="0 0 12 12"><circle cx="6" cy="6" r="6" fill="var(--red)"/><path d="M3.2 6.2l1.9 1.9 3.7-3.8" fill="none" stroke="#fff" stroke-width="1.5"/></svg>Life</li>
        <li><svg class="tick" viewBox="0 0 12 12"><circle cx="6" cy="6" r="6" fill="var(--red)"/><path d="M3.2 6.2l1.9 1.9 3.7-3.8" fill="none" stroke="#fff" stroke-width="1.5"/></svg>Business Automobile</li>
        <li><svg class="tick" viewBox="0 0 12 12"><circle cx="6" cy="6" r="6" fill="var(--red)"/><path d="M3.2 6.2l1.9 1.9 3.7-3.8" fill="none" stroke="#fff" stroke-width="1.5"/></svg>Health</li>
        <li><svg class="tick" viewBox="0 0 12 12"><circle cx="6" cy="6" r="6" fill="var(--red)"/><path d="M3.2 6.2l1.9 1.9 3.7-3.8" fill="none" stroke="#fff" stroke-width="1.5"/></svg>Commercial Excess Liability</li>
      </ul>
    </div>
  </section>

  <section class="testimonial-row">
    <div class="meeting-photo" role="img" aria-label="Photo of a business team meeting around a table"></div>
    <blockquote class="testimonial">
      <p class="quote">The Tavenmork Company has consistently responded to the needs of our business, finding us well priced policies without sacrificing coverage. They always respond to our needs quickly and effectively, provide great consultation, are knowledgeable, and care greatly about our business and success.</p>
      <p class="quote-name">DANIEL HARROW</p>
      <p class="quote-role">Business Owner</p>
    </blockquote>
  </section>

  <footer class="footer">
    <span class="footer-url">www.tavenmork.com</span>
    <span class="footer-brand"><span class="footer-dot"></span><span class="footer-name">Tavenmork</span></span>
  </footer>
</main>
</body>
</html>
```